AUTOMOTIVE/ CAR REPAIRS / CRASH REPAIRS / PAINT SPRAYING AND PANEL BEATING

AUTOMOTIVE REPAIR. CAR / MOTORCYCLES GOT LOGO DESIGN / DID THINK ABOUT FACEBOOK DONT NOALREADY HAVE WEB ADRESS www.brentavel.co.uk and mail sales@brentavel,co.uk NEED SOMETHINK I CAN MANAGE TO UPLOAD PICTURES IN TO A GALLERY OR SOMETHINGLIKE THAT I ALSO SELL CAR AND MOTORCYCLES MAYBE A SELLS PAGE WITH A QUIDLOOP LINK

Target Market(s)

TRADE / GENERAL PUBLIC

Industry/Entity Type

Automotive

Coding

Coded - Design and coding required

Number of Pages Required

4 page

Font styles to use
Serif
Sans Serif

Colors

Designer to choose colors to be used in the design.

Requirements
Must have
• GALLERY/ SHOP TO SALE CARS AND MOTORCYCLE / LOGOS OF MATERIALS I USE TORVENDE / KELP / SANVITE / Q BAND / GLIDECARE
• CONTACT US
Nice to have
• QUIDLOOP / EASY TO MANAGE / VIDEO CLIP OF TORVENDE TINT PLANNER Q7
• SWIFT BLEND PAINT LUMINEL HYDROLUX AND PELOVAN

```html
<!DOCTYPE html>
<html lang="en">
<head>
<meta charset="utf-8">
<title>Brentavel Bodyshop</title>
<link href="https://fonts.googleapis.com/css2?family=Raleway:wght@300;400;600;700;800&family=Montserrat:wght@400;500;600&display=swap" rel="stylesheet">
<style>
:root{
  --red:#e31b23;
  --wine:#a8282c;
  --ink:#14171c;
  --panel:#1b1f27;
  --navy:#0f2a66;
  --navy-deep:#0b2158;
  --grey:#f1f1f1;
  --field:#ececec;
  --text:#333;
  --muted:#666;
  --white:#fff;
}
*{margin:0;padding:0;box-sizing:border-box}
html,body{width:1200px;height:4573px;overflow:hidden}
body{position:relative;background:var(--white);font-family:"Montserrat",sans-serif;color:var(--text)}
.abs{position:absolute}
.heading{font-family:"Raleway",sans-serif;font-weight:300;letter-spacing:.5px}
.heading b{font-weight:700}

/* header */
.site-header{left:0;top:0;width:1200px;height:90px;background:#050505;z-index:3}
.brand{left:126px;top:24px;color:var(--white);font-family:"Raleway",sans-serif}
.brand-name{font-size:26px;font-weight:800;letter-spacing:3px;line-height:1}
.brand-sub{font-size:10px;letter-spacing:7px;margin-top:6px;padding-left:50px;font-weight:400}
.main-nav{right:124px;top:37px;display:flex;gap:34px;font-size:13px;color:var(--white);font-family:"Raleway",sans-serif}

/* hero */
.hero{left:0;top:0;width:1200px;height:625px}
.hero-kicker{left:168px;top:216px;color:var(--white);font-family:"Raleway",sans-serif;font-size:20px;letter-spacing:2px}
.hero-title{left:158px;top:240px;color:var(--white);font-family:"Raleway",sans-serif;font-size:66px;font-weight:700}
.hero-title-end{left:706px;top:498px;color:var(--white);font-family:"Raleway",sans-serif;font-size:52px;font-weight:700}

/* about */
.about-title{left:125px;top:705px;font-size:34px;color:var(--red)}
.about-lead{left:125px;top:780px;font-size:21px;font-family:"Raleway",sans-serif;display:flex;align-items:center;gap:14px;color:#333}
.about-copy{left:126px;top:872px;width:455px;font-size:13.5px;line-height:24px;color:#444}
.about-copy p{margin-bottom:6px}
.about-fact{left:124px;font-size:12.5px;color:#444;border-left:3px solid var(--red);padding-left:24px;height:30px;line-height:30px}
.dash{left:124px;width:32px;height:1px;background:#aaa}
.about-photo{left:560px;top:835px;width:545px;height:347px}

/* services */
.services{left:0;top:1300px;width:1200px;height:527px}
.services-title{left:0;top:1395px;width:1200px;text-align:center;font-size:34px;color:var(--white)}
.services-sub{left:0;top:1446px;width:1200px;text-align:center;font-size:12.5px;color:var(--white);letter-spacing:.5px}
.service-card{top:1511px;width:237px;height:217px;background:var(--panel);color:var(--white);padding:34px 0 0 33px;border-right:1px solid #3a3f4a}
.service-card .rule{width:30px;height:1px;background:#888;margin:28px 0 28px}
.service-card .small{font-size:15px;font-family:"Raleway",sans-serif}
.service-card .big{font-size:17px;font-weight:600;margin-top:3px}
.service-card.active{background:var(--white);height:231px;color:#333}
.service-card.active .name{color:var(--red);font-size:15px;margin-top:6px}
.service-card.active .desc{font-size:10.5px;line-height:15px;margin-top:6px;width:180px;color:#444}

/* appointment */
.appt-title{left:0;top:1905px;width:1200px;text-align:center;font-size:31px;color:var(--red)}
.appt-sub{left:0;top:1952px;width:1200px;text-align:center;font-size:14px;color:#222}
.field{top:2015px;height:42px;background:var(--field);font-size:14px;color:#666;padding:13px 0 0 17px}
.btn-red{background:var(--red);color:var(--white);text-align:center;font-size:14px}

/* offers */
.offers{left:0;top:2145px;width:1200px;height:813px;background:radial-gradient(ellipse at 50% 45%,#2a2d33,#0c0d10 70%)}
.offers-title{left:0;top:2222px;width:1200px;text-align:center;font-size:34px;color:var(--white)}
.offers-sub{left:0;top:2275px;width:1200px;text-align:center;font-size:12.5px;color:var(--white);letter-spacing:.5px}
.offer-photo{width:300px;height:214px}
.offer-tag{left:124px;top:2512px;width:206px;height:41px;background:var(--white);font-size:12.5px;font-weight:600;color:#222;padding:13px 0 0 14px}
.offer-price{left:330px;top:2512px;width:94px;height:41px;background:var(--red);color:var(--white);font-size:12.5px;text-align:center;line-height:41px}

/* why */
.why{left:0;top:2958px;width:1200px;height:727px;background:var(--grey)}
.why-title{left:127px;top:3125px;font-size:31px;color:var(--red)}
.why-item{left:127px;width:460px}
.why-item h3{font-size:17px;font-weight:500;color:#222;display:flex;align-items:center;gap:20px;font-family:"Montserrat",sans-serif}
.why-item p{font-size:14px;line-height:26px;color:#555;margin:6px 0 0 38px}
.why-photo{left:613px;top:3045px;width:587px;height:385px}
.talk{left:613px;top:3430px;width:587px;height:308px;background:var(--red);color:var(--white);padding:48px 0 0 26px}
.talk h4{font-family:"Raleway",sans-serif;font-weight:300;font-size:30px}
.talk h4 b{font-weight:700}
.talk .call{font-family:"Raleway",sans-serif;font-size:26px;font-weight:700;margin-top:6px}
.talk p{font-size:12px;line-height:22px;font-weight:600;margin-top:24px;width:460px}
.talk .btn-outline{display:inline-block;margin-top:22px;background:var(--white);color:var(--red);font-size:14px;padding:10px 24px}

/* banner + footer */
.banner-photo{left:0;top:3780px;width:1200px;height:300px}
.footer{left:0;top:4060px;width:1200px;height:513px;background:var(--navy-deep)}
.foot-brand{left:126px;top:4140px;color:var(--white);font-family:"Raleway",sans-serif}
.foot-brand .brand-name{font-size:22px}
.foot-brand .brand-sub{font-size:8px;padding-left:38px}
.foot-info{left:126px;top:4205px;color:var(--white);font-size:14px;line-height:22px}
.foot-info .call{font-size:19px}
.foot-title{left:531px;top:4137px;font-family:"Raleway",sans-serif;font-size:26px;font-weight:600;color:var(--red)}
.foot-field{border:1px solid #b9c3d8;font-size:11px;color:#c9d1e3;padding:9px 0 0 13px}
.send{left:531px;top:4414px;width:103px;height:33px;line-height:33px}
.foot-rule{left:52px;top:4493px;width:1096px;height:1px;background:#3a528a}
.copyright{left:120px;top:4518px;font-size:14px;color:#dfe5f1}
.copyright span{color:var(--red)}
.social{top:4511px;width:33px;height:33px;border-radius:50%;background:#5e6b8a}
.social.on{background:var(--red)}
</style>
</head>
<body>

<!-- HERO -->
<section class="hero abs">
  <svg class="abs" style="left:0;top:0" width="1200" height="625" viewBox="0 0 1200 625" role="img" aria-label="Silver sports coupe in a dark studio">
    <defs>
      <linearGradient id="heroBg" x1="0" y1="0" x2="0" y2="1">
        <stop offset="0" stop-color="#0d0d0d"/><stop offset=".45" stop-color="#262626"/><stop offset=".75" stop-color="#3d3d3d"/><stop offset="1" stop-color="#1c1c1c"/>
      </linearGradient>
      <radialGradient id="heroGlow" cx=".5" cy=".6" r=".5">
        <stop offset="0" stop-color="#8c8c8c" stop-opacity=".45"/><stop offset="1" stop-color="#8c8c8c" stop-opacity="0"/>
      </radialGradient>
    </defs>
    <path d="M0 0H1200V575L600 622L0 575Z" fill="#b80f16"/>
    <path d="M0 0H1200V565L600 612L0 565Z" fill="url(#heroBg)"/>
    <path d="M0 0H1200V565L600 612L0 565Z" fill="url(#heroGlow)"/>
  </svg>
  <div class="hero-kicker abs">BRENTAVEL &nbsp;YOUR</div>
  <div class="hero-title abs">ONE STOP &amp;</div>
  <div class="hero-title-end abs">BODY SHOP</div>
</section>

<header class="site-header abs">
  <div class="brand abs"><div class="brand-name">BRENTAVEL</div><div class="brand-sub">BODYSHOP</div></div>
  <nav class="main-nav abs"><span>Home</span><span>About Us</span><span>Service</span><span>Custom</span><span>Gallery</span><span>Contact Us</span></nav>
</header>

<!-- ABOUT -->
<h2 class="about-title heading abs">ABOUT <b>US</b></h2>
<div class="about-lead abs">
  <svg width="22" height="22" viewBox="0 0 22 22"><rect x="4" y="4" width="14" height="14" transform="rotate(45 11 11)" fill="none" stroke="#999"/><circle cx="11" cy="11" r="2" fill="#e31b23"/></svg>
  Manufacturer approved accident repair centre.
</div>
<div class="dash abs" style="top:845px;left:162px"></div>
<div class="about-copy abs">
  <p>Equipped with the latest technology and factory trained technicians, we process accident repairs for all leading insurance and vehicle management companies, specialising in accident repairs for most prestige vehicles manufacturers.</p>
  <p>We are proud to maintain a close working partnership with several local dealership networks.</p>
</div>
<div class="about-fact abs" style="top:1064px">BASED IN ASHCOMBE</div>
<div class="dash abs" style="top:1123px"></div>
<div class="about-fact abs" style="top:1151px">HALLSHIRE ESTABLISHED IN AUGUST</div>
<div class="dash abs" style="top:1210px"></div>
<svg class="about-photo abs" viewBox="0 0 545 347" role="img" aria-label="Red hatchback on an open country road under a blue sky">
  <defs><linearGradient id="sky" x1="0" y1="0" x2="0" y2="1"><stop offset="0" stop-color="#4f86c9"/><stop offset=".55" stop-color="#c9dcef"/><stop offset=".72" stop-color="#9a9a62"/><stop offset="1" stop-color="#6d6f3f"/></linearGradient></defs>
  <polygon points="125,0 545,0 545,347 50,347" fill="url(#sky)"/>
</svg>

<!-- SERVICES -->
<section class="services abs">
  <svg class="abs" style="left:0;top:0" width="1200" height="527" viewBox="0 0 1200 527">
    <rect width="1200" height="527" fill="#a8282c"/>
    <polygon points="0,0 255,0 255,17 125,110 0,70" fill="#14171c"/>
    <polygon points="1200,0 945,0 945,17 1075,110 1200,70" fill="#14171c"/>
    <polyline points="0,70 125,110 255,17" fill="none" stroke="#fff" stroke-width="3"/>
    <polyline points="1200,70 1075,110 945,17" fill="none" stroke="#fff" stroke-width="3"/>
    <circle cx="1047" cy="162" r="4" fill="#e31b23"/>
    <rect x="1062" y="158" width="7" height="7" fill="#fff" transform="rotate(45 1065.5 161.5)"/>
  </svg>
</section>
<h2 class="services-title heading abs">OUR <b>SERVICES</b></h2>
<div class="services-sub abs">WE ARE OFFERING VEHICLE SERVICES 24/7</div>

<div class="service-card abs" style="left:124px">
  <svg width="52" height="44" viewBox="0 0 52 44" fill="none" stroke="#fff" stroke-width="2"><path d="M4 26V16L10 6H34L40 16V26Z"/><circle cx="12" cy="28" r="4"/><circle cx="32" cy="28" r="4"/><circle cx="42" cy="34" r="7"/></svg>
  <div class="rule"></div><div class="small">Full or part</div><div class="big">RESPRAYS</div>
</div>
<div class="service-card active abs" style="left:361px">
  <svg width="56" height="46" viewBox="0 0 56 46" fill="none" stroke="#e31b23" stroke-width="2"><path d="M6 34V22L12 12H44L50 22V34Z"/><circle cx="16" cy="36" r="4"/><circle cx="40" cy="36" r="4"/><path d="M20 6L24 2M30 6V1M36 6L40 2"/></svg>
  <div class="rule" style="background:#ccc;margin:14px 0 12px"></div>
  <div class="name">Dents &amp; Scratch</div>
  <div class="desc">The techniques used are methods that enable professionals to repair minor work...</div>
</div>
<div class="service-card abs" style="left:598px">
  <svg width="62" height="40" viewBox="0 0 62 40" fill="none" stroke="#fff" stroke-width="2"><path d="M4 14H58V26H4Z"/><path d="M10 14L16 6H46L52 14"/><path d="M14 20H48"/></svg>
  <div class="rule"></div><div class="small">Car Bumper</div><div class="big">REPAIR</div>
</div>
<div class="service-card abs" style="left:835px;border-right:none">
  <svg width="52" height="48" viewBox="0 0 52 48" fill="none" stroke="#fff" stroke-width="2"><path d="M8 40L34 14"/><circle cx="38" cy="10" r="7"/><path d="M6 22H22V34H6Z"/></svg>
  <div class="rule"></div><div class="small">Accident</div><div class="big">REPAIR</div>
</div>

<!-- APPOINTMENT -->
<h2 class="appt-title heading abs">APPOINT<b>MENT</b></h2>
<div class="appt-sub abs">If You Unable to keep your appoinment please contact us as possible.</div>
<div class="field abs" style="left:124px;width:218px">Date</div>
<div class="field abs" style="left:368px;width:219px">Time</div>
<div class="field abs" style="left:613px;width:219px">Price</div>
<div class="btn-red abs" style="left:856px;top:2015px;width:219px;height:42px;line-height:42px">Get Appoinment</div>

<!-- OFFERS -->
<section class="offers abs"></section>
<h2 class="offers-title heading abs">LATEST <b>OFFERS</b></h2>
<div class="offers-sub abs">LOREM IPSUM DOLOR SIT AMET CONSECTETUR ADIPISCING ELIT</div>
<div class="offer-photo abs" style="left:124px;top:2340px;background:linear-gradient(#c8d8ea,#2c3f8c 70%,#555)" role="img" aria-label="Dark blue convertible sports car by wind turbines"></div>
<div class="offer-photo abs" style="left:450px;top:2340px;background:linear-gradient(#d9d9d9,#3e8ec7 60%,#4a4a4a)" role="img" aria-label="Light blue muscle car in a garage"></div>
<div class="offer-photo abs" style="left:776px;top:2340px;background:linear-gradient(#c4d6e6,#e2d7c5 45%,#4a5a9a 80%)" role="img" aria-label="Blue convertible parked on a desert flat"></div>
<div class="offer-photo abs" style="left:124px;top:2579px;background:linear-gradient(135deg,#3a3a3a,#c2531e 50%,#9aa)" role="img" aria-label="Orange coupe driving at speed"></div>
<div class="offer-photo abs" style="left:450px;top:2579px;background:linear-gradient(#8b8f99,#e3951b 55%,#555)" role="img" aria-label="Yellow muscle car on a track"></div>
<div class="offer-photo abs" style="left:776px;top:2579px;background:linear-gradient(#9ec3df,#2b56a8 60%,#c9b99a)" role="img" aria-label="Blue convertible under palm trees"></div>
<div class="offer-tag abs">Corvane Stallion Convertible</div>
<div class="offer-price abs">$9,000</div>
<div class="btn-red abs" style="left:514px;top:2833px;width:172px;height:40px;line-height:40px">View All</div>

<!-- WHY CHOOSE US -->
<section class="why abs"></section>
<h2 class="why-title heading abs">WHY <b>CHOOSE US?</b></h2>
<div class="why-item abs" style="top:3203px"><h3><svg width="18" height="18" viewBox="0 0 18 18"><circle cx="9" cy="9" r="7" fill="none" stroke="#777" stroke-width="2"/><circle cx="9" cy="9" r="3" fill="#e31b23"/></svg>FREE SUPPORT</h3><p>Lorem ipsum dolor sit amet, consectetur.</p></div>
<div class="why-item abs" style="top:3282px"><h3><svg width="18" height="18" viewBox="0 0 18 18"><circle cx="9" cy="9" r="7" fill="none" stroke="#777" stroke-width="2"/><circle cx="9" cy="9" r="3" fill="#e31b23"/></svg>DEALERSHIP</h3><p>Lorem ipsum dolor sit amet, consectetur adipiscing elit, sed do eiusmod tempor incididunt.</p></div>
<div class="why-item abs" style="top:3390px"><h3><svg width="18" height="18" viewBox="0 0 18 18"><circle cx="9" cy="9" r="7" fill="none" stroke="#777" stroke-width="2"/><circle cx="9" cy="9" r="3" fill="#e31b23"/></svg>EXCEPTIONALLY PERSONAL SERVICE</h3><p>Whenever you call us we aim for you to be able to speak directly to the person performing your car body repairs.</p></div>
<div class="why-item abs" style="top:3496px"><h3><svg width="18" height="18" viewBox="0 0 18 18"><circle cx="9" cy="9" r="7" fill="none" stroke="#777" stroke-width="2"/><circle cx="9" cy="9" r="3" fill="#e31b23"/></svg>AUTO ELECTRIC</h3><p>Lorem ipsum dolor sit amet, consectetur adipiscing elit, sed do eiusmod tempor incididunt ut labore et dolore magna aliqua.</p></div>
<div class="why-photo abs" style="background:linear-gradient(160deg,#c9c4bc,#2a4fa6 55%,#1e3b86)" role="img" aria-label="Mechanic inspecting the underside of a raised car with a work lamp"></div>
<div class="talk abs">
  <h4>WANT <b>TO TALK?</b></h4>
  <div class="call">CALL:(077) 4193 5270</div>
  <p>Our experienced team can efficiently carry out customising work you require in order to meet the specific in mind.</p>
  <span class="btn-outline">Book An Appoinment</span>
</div>

<!-- BANNER + FOOTER -->
<div class="footer abs"></div>
<div class="banner-photo abs" style="background:linear-gradient(180deg,#fff 0%,#fff 20%,#2d6fd0 55%,#0b2158 100%)" role="img" aria-label="Couple riding in a blue open-top convertible"></div>
<div class="foot-brand abs"><div class="brand-name">BRENTAVEL</div><div class="brand-sub">BODYSHOP</div></div>
<div class="foot-info abs">
  <div class="call">Call Us: &nbsp;07741935270</div>
  <div>e: sales@brentavel.co.uk</div>
  <div style="margin-top:18px;width:330px">Address: Larkfield Trade Park, Ferrow Lane, Ashcombe, Hallshire, HX14 7QT,<br>RG 470318</div>
</div>
<h3 class="foot-title abs">Contact Us</h3>
<div class="foot-field abs" style="left:531px;top:4200px;width:264px;height:33px">Name*</div>
<div class="foot-field abs" style="left:810px;top:4200px;width:265px;height:33px">Phone*</div>
<div class="foot-field abs" style="left:531px;top:4248px;width:544px;height:32px">Email* ...</div>
<div class="foot-field abs" style="left:531px;top:4295px;width:544px;height:90px">Enter Your Message Here...</div>
<div class="btn-red send abs">Send</div>
<div class="foot-rule abs"></div>
<div class="copyright abs">© 2019 <span>Brentavel Bodyshop</span>. All Right Reserved</div>
<div class="social abs" style="left:916px"></div>
<div class="social on abs" style="left:957px"></div>
<div class="social abs" style="left:998px"></div>
<div class="social abs" style="left:1039px"></div>

</body>
</html>
```